Restyle Company web site and logo

we need a wordpress design beacause after few year we need to refresh our company web site(www.vorantelabs.net) & logo. We are a small company called KP Advisory focused on business intellegence, data quality, data integration, etc and based on Legnago (small town near to Verona (italy)).
During the 2014 we add to our skill develop project for MDM and Procurement.
We are Young (avg 30 years old). We want to change our logo and color templete to communicate to all cumstomer professional skill, precision and passion.

--- UPDATE --
The new site can be complitile different from the actual website.
The new Logo is now available.
Updates

Target Market(s)

B2B, mid size market, professional account

Industry/Entity Type

It Company

Font styles to use
Sans Serif

Colors
acd037
3277b5

Requirements
Must have
• Simple and clean/clear image colur. Professional site. it need to rapresent trust site.
• Must be responsive desk/mobile.
Nice to have
• different color area for different kind off business line.
• slider image.
Should not have
• classical image

```html
<!DOCTYPE html>
<html lang="en">
<head>
<meta charset="utf-8">
<title>KP Advisory</title>
<link rel="stylesheet" href="https://fonts.googleapis.com/css2?family=Arimo:wght@400;700&family=Open+Sans:wdth,wght@75,300;75,400&display=swap">
<style>
:root{
  --blue:#0a6aa8;
  --blue-dark:#075a90;
  --blue-link:#1e6fae;
  --green:#9cc420;
  --ink:#222;
  --grey-text:#666;
  --band:#e6e6e6;
  --line:#dcdcdc;
  --page:#f1f1f1;
}
*{box-sizing:border-box;margin:0;padding:0}
html,body{width:821px;height:1200px;overflow:hidden}
body{background:var(--page);font-family:"Arimo",Arial,sans-serif;color:var(--ink);position:relative}
.abs{position:absolute}
.cond{font-family:"Open Sans",Arial,sans-serif;font-stretch:75%;font-weight:300}

/* header */
.site-header{left:0;top:0;width:821px;height:98px;background:linear-gradient(#fdfdfd,#ececec)}
.brand{left:76px;top:28px;display:flex;align-items:center;gap:8px;font-size:17px;font-weight:700;color:var(--blue)}
.brand-dot{width:22px;height:22px;border-radius:50%;background:var(--green)}
.connect{right:70px;top:14px;font-size:11.5px;color:#333;display:flex;align-items:center;gap:5px}
.connect i{display:inline-block;width:14px;height:14px;background:var(--blue-link);border-radius:2px}
.call{right:70px;top:37px;font-size:11.5px;color:#333}
.call span{color:var(--blue-link)}
.main-nav{left:253px;top:60px;width:500px;height:30px;background:linear-gradient(#aed63a,#8fbf16);display:flex;border-radius:2px}
.main-nav a{flex:1;text-align:center;line-height:30px;font-size:12px;color:#1c2a06;text-decoration:none;border-right:1px solid #84ad18;white-space:nowrap}
.main-nav a:last-child{border-right:0}

/* hero */
.hero{left:0;top:102px;width:821px;height:258px;background:linear-gradient(90deg,#0b6ba9 0%,#0a6aa8 50%,#0f5f95 100%);overflow:hidden}
.hero-photo{left:436px;top:0;width:250px;height:258px;background:radial-gradient(ellipse at 60% 45%,#8fd2f2 0%,#3d9bd0 35%,#12426a 75%,#0a2f50 100%)}
.hero-title{left:79px;top:56px;font-size:33px;font-weight:400;color:#fff;letter-spacing:.5px}
.hero-sub{left:77px;top:96px;font-size:32px;line-height:38px;color:#fff}

/* services */
.services{left:0;top:364px;width:821px;height:114px;background:var(--band)}
.service-icon{top:18px;flex:none}
.service-body{top:16px;width:160px}
.service-body h3{font-weight:400;font-size:14.5px;line-height:18px;margin-bottom:3px;color:#222}
.service-body p{font-size:8.6px;line-height:10.5px;color:#444}

/* content panel */
.panel{left:62px;top:501px;width:691px;height:640px;background:#fff;border:1px solid var(--line)}
.section-title{font-size:30px;font-weight:300;color:#222;letter-spacing:.3px;line-height:36px}
.lead{left:81px;top:560px;width:400px;font-size:13px;line-height:17px;color:#111}
.intro{left:81px;top:601px;width:405px;font-size:10px;line-height:16px;color:var(--grey-text)}
.team-card{top:760px;width:104px;text-align:center}
.team-photo{width:104px;height:70px;border:1px solid var(--line);background:linear-gradient(135deg,#e9eef3,#9fb4c8 55%,#2a3c55)}
.team-card p{font-size:9px;line-height:11px;color:#333;margin-top:9px}
.team-card a{display:block;font-size:8.5px;color:var(--blue-link);text-decoration:none;margin-top:6px}
.arrow{width:12px;height:12px;border-radius:50%;background:#cfcfcf}
.case-title{left:83px;top:968px;font-size:14px;font-weight:400;color:var(--blue-link)}
.case-text{left:83px;top:992px;width:390px;font-size:8.9px;line-height:11.2px;color:#222}
.more-btn{left:83px;top:1054px;width:62px;height:17px;background:linear-gradient(#a9d434,#86b612);border-radius:2px;box-shadow:1px 1px 0 #5e7f0c;color:#fff;font-size:9px;line-height:17px;text-align:center}

/* news */
.news{left:537px;width:200px;display:flex;gap:12px}
.news-date{width:46px;height:60px;background:var(--blue);color:#fff;text-align:center;position:relative;flex:none}
.news-date::after{content:"";position:absolute;right:-6px;top:8px;border:6px solid transparent;border-left-color:var(--blue);border-right:0}
.news-date b{display:block;font-family:"Open Sans",Arial,sans-serif;font-stretch:75%;font-weight:300;font-size:25px;line-height:30px;padding-top:3px}
.news-date span{font-family:"Open Sans",Arial,sans-serif;font-stretch:75%;font-weight:300;font-size:15px}
.news h4{font-weight:400;font-size:11px;line-height:13px;color:#111;margin:1px 0 5px}
.news p{font-size:9px;line-height:11px;color:#555}

.question{left:537px;top:815px;width:197px;height:91px;border:1px solid var(--line);background:#fff}
.question-text{left:12px;top:10px;font-size:15px;line-height:18px;color:#222}
.question-photo{right:0;top:0;width:70px;height:65px;background:linear-gradient(160deg,#f2e6de,#c9a79a 60%,#6e5146)}
.question-call{left:0;bottom:0;width:100%;height:25px;background:var(--green);color:#fff;font-size:15px;line-height:25px;text-align:center}

.tags{left:544px;top:986px;width:110px;line-height:15px;color:#1d3f8a}
.tags span{text-decoration:underline;margin-right:2px}

/* footer */
.site-footer{left:0;top:1141px;width:821px;height:59px;background:var(--blue);border-top:3px solid var(--blue-dark)}
.footer-info{left:79px;top:14px;font-size:8.8px;line-height:14px;color:#fff}
.footer-brand{right:80px;top:20px;font-size:10px;font-weight:700;color:#fff}
</style>
</head>
<body>

<header class="site-header abs">
  <div class="brand abs"><span class="brand-dot"></span>KP Advisory</div>
  <div class="connect abs">Connect with us: <i></i><i></i></div>
  <div class="call abs">Call: <span>0245 118 2730</span></div>
  <nav class="main-nav abs">
    <a href="#">Home</a><a href="#">Business Partner</a><a href="#">References</a><a href="#">Work with us</a><a href="#">Contacts</a>
  </nav>
</header>

<section class="hero abs">
  <div class="hero-photo abs" role="img" aria-label="Close-up photograph of a business handshake tinted in blue"></div>
  <h1 class="hero-title abs">KP ADVISORY</h1>
  <p class="hero-sub abs cond">Get the Desired Information at the<br>Right Time and in the Correct Form.</p>
</section>

<section class="services abs">
  <svg class="service-icon abs" style="left:62px" width="34" height="30" viewBox="0 0 34 30"><rect x="1" y="3" width="32" height="20" rx="2" fill="var(--blue)"/><rect x="4" y="6" width="26" height="14" fill="#3a8cc4"/><rect x="14" y="23" width="6" height="4" fill="var(--blue)"/><rect x="9" y="27" width="16" height="2" fill="var(--blue)"/></svg>
  <div class="service-body abs" style="left:109px"><h3>Evolution support</h3><p>Do not let the problems curb your business. Evolution support was established with the aim to help our clients in all stages of the project...</p></div>

  <svg class="service-icon abs" style="left:301px" width="32" height="30" viewBox="0 0 32 30"><path d="M2 24a14 14 0 0 1 28 0z" fill="var(--blue)"/><circle cx="16" cy="22" r="3" fill="#fff"/><path d="M16 22 L23 12" stroke="#fff" stroke-width="2"/><circle cx="7" cy="19" r="1.5" fill="#fff"/><circle cx="10" cy="13" r="1.5" fill="#fff"/><circle cx="16" cy="11" r="1.5" fill="#fff"/><circle cx="25" cy="19" r="1.5" fill="#fff"/></svg>
  <div class="service-body abs" style="left:342px;width:160px"><h3>Corporate Performance Management</h3><p>The information that drives your business. How many people in your company have the right information at the right time</p></div>

  <svg class="service-icon abs" style="left:548px" width="32" height="30" viewBox="0 0 32 30"><circle cx="16" cy="15" r="13" fill="var(--blue)"/><path d="M16 15 L16 2 M16 15 L27 21 M16 15 L5 21" stroke="#fff" stroke-width="2"/></svg>
  <div class="service-body abs" style="left:594px"><h3>Business Intelligence</h3><p>Do not let the problems curb your business. Evolution support was established with the aim to help our clients in all stages of the project...</p></div>
</section>

<main>
  <div class="panel abs"></div>

  <h2 class="section-title cond abs" style="left:80px;top:512px">WELCOME!</h2>
  <p class="lead abs">How many people in your company have the desired information at the right time and in the correct form?</p>
  <p class="intro abs">For a company it is essential to exploit the wealth of information available to make them accessible to their managers in order to help them in choosing the right business strategies (see the trend of performance, generate estimates, assume future scenarios and future strategies of response.) KP Advisory helps you to manage this process as simple and fast!</p>

  <h2 class="section-title cond abs" style="left:80px;top:694px">OUR TEEM</h2>
  <span class="arrow abs" style="left:88px;top:794px"></span>
  <div class="team-card abs" style="left:107px"><div class="team-photo" role="img" aria-label="Portrait photograph of a team member on the phone"></div><p>Sed faucibus vitae augue at faucibus.</p><a href="#">Learn more &gt;&gt;</a></div>
  <div class="team-card abs" style="left:234px"><div class="team-photo" role="img" aria-label="Portrait photograph of a team member on the phone"></div><p>Sed faucibus vitae augue at faucibus.</p><a href="#">Learn more &gt;&gt;</a></div>
  <div class="team-card abs" style="left:361px"><div class="team-photo" role="img" aria-label="Portrait photograph of a team member on the phone"></div><p>Sed faucibus vitae augue at faucibus.</p><a href="#">Learn more &gt;&gt;</a></div>
  <span class="arrow abs" style="left:469px;top:794px"></span>

  <h2 class="section-title cond abs" style="left:80px;top:920px">CUSTOMER CASE HISTORY</h2>
  <h3 class="case-title abs">Donec blandit luctus massa</h3>
  <p class="case-text abs">Lorem ipsum dolor sit amet, consectetur adipiscing elit. Vivamus egestas fermentum tempor. Vivamus sit amet elit sit amet risus vehicula scelerisque. Donec blandit luctus massa, in scelerisque ex pellentesque et. Vivamus egestas fermentum tempor. Vivamus sit amet elit sit amet risus vehicula scelerisque. Donec blandit luctus massa, in scelerisque ex pellentesque et.</p>
  <div class="more-btn abs">More</div>

  <h2 class="section-title cond abs" style="left:534px;top:518px">RECENT NEWS</h2>
  <article class="news abs" style="top:564px"><div class="news-date"><b>06</b><span>OCT</span></div><div><h4>NORDA vince il Clearpath Swiss Inno…</h4><p>Lorem ipsum dolor sit amet, consectetur adipiscing elit.</p></div></article>
  <article class="news abs" style="top:643px"><div class="news-date"><b>06</b><span>OCT</span></div><div><h4>NORDA Spring Tour 2012</h4><p>Lorem ipsum dolor sit amet, consectetur adipiscing elit.</p></div></article>
  <article class="news abs" style="top:719px"><div class="news-date"><b>06</b><span>OCT</span></div><div><h4>Nunc non bibendum nisl.</h4><p>Lorem ipsum dolor sit amet, consectetur adipiscing elit. Nullam condimentum libero quis est</p></div></article>

  <aside class="question abs">
    <div class="question-photo abs" role="img" aria-label="Photograph of a support operator wearing a headset"></div>
    <p class="question-text abs">Have any<br>Questions?</p>
    <div class="question-call abs">Call us: 0245 118 2730</div>
  </aside>

  <h2 class="section-title cond abs" style="left:535px;top:942px">TAG CLOUD</h2>
  <div class="tags abs">
    <span style="font-size:15px">prism</span><span style="font-size:7px">utenti</span><br>
    <span style="font-size:13px">norda</span><span style="font-size:11px">clearpath</span><br>
    <span style="font-size:6px">software</span><span style="font-size:16px">dati</span><span style="font-size:5px">calendario</span><br>
    <span style="font-size:13px">report</span><span style="font-size:12px">business</span><br>
    <span style="font-size:8px">reports</span><span style="font-size:5px">webportal.net</span>
  </div>
</main>

<footer class="site-footer abs">
  <p class="footer-info abs">KP Advisory S.r.l. - Via dei Roveri, 7/B - 37128 Castelmora (VR)<br>© Copyright KP Advisory 2014 All Rights Reserved.</p>
  <div class="footer-brand abs">KP Advisory</div>
</footer>

</body>
</html>
```